Design a modern, premium front panel for a stand-up pouch

Design a modern, premium front for a stand-up pouch for VELUTRA. Product is for Urine/vomit/runny stool incidents indoors; quick cleanups before smell sets; nighttime/elderly pet accidents; travel/car mishaps.

It must instantly show it’s for dogs & cats and include three small step icons with labels: Sprinkle → Wait 1–5 min → Sweep. Front copy to include: VELUTRA, descriptor “Mineral Instant Absorber – for Dogs & Cats”, one benefits line “Fragrance-Free • 100 % Mineral • Odor-Binding • Low-Dust

Goal: clear who/what/how in under 3 seconds
Deliverables: AI/PDF + a pouch mockup;

Target Market(s)

• Dog & cat households in apartments/homes; new pet parents, senior pets, multi-pet homes. • Cleanliness & odor-sensitive buyers (allergies/asthma, fragrance-free preference). • Surfaces at risk: carpets/rugs, sofas, mattresses, car interiors.

Industry/Entity Type

Pet e-commerce and retail

Font styles to use
Other font styles liked:
• like attached images

Requirements
Nice to have
• light background, eco friendly

```html
<!DOCTYPE html>
<html lang="en">
<head>
<meta charset="utf-8">
<title>VELUTRA Mineral Instant Absorber – Pouch Front</title>
<link href="https://fonts.googleapis.com/css2?family=Josefin+Sans:wght@300&family=Barlow+Semi+Condensed:wght@600;700&family=Fredoka:wght@600&display=swap" rel="stylesheet">
<style>
  :root{
    --stage:#d7ece6;
    --panel-top:#ffffff;
    --panel-bottom:#f2efe5;
    --green:#4db694;
    --green-deep:#3fa483;
    --purple:#774a96;
    --white:#ffffff;
  }
  *{margin:0;padding:0;box-sizing:border-box}
  html,body{width:1200px;height:1200px;overflow:hidden}
  body{background:var(--stage);position:relative;font-family:"Barlow Semi Condensed",sans-serif}
  .pouch-front{
    position:absolute;left:249px;top:40px;width:702px;height:1120px;
    background:linear-gradient(180deg,var(--panel-top) 0%,var(--panel-bottom) 85%);
    border-radius:22px 22px 6px 6px;overflow:hidden;
  }
  .seal-line{position:absolute;left:40px;right:40px;top:113px;height:2px;background:#ecebe6}
  .brand{
    position:absolute;left:0;right:0;top:205px;text-align:center;
    font-family:"Josefin Sans",sans-serif;font-weight:300;font-size:104px;
    letter-spacing:14px;padding-left:14px;color:var(--green);line-height:1;
  }
  .descriptor-kicker{
    position:absolute;left:0;right:0;top:376px;text-align:center;line-height:1;
    font-weight:700;font-size:19px;letter-spacing:6px;padding-left:6px;color:var(--purple);
  }
  .descriptor-main{
    position:absolute;left:0;right:0;top:402px;text-align:center;
    font-weight:700;font-size:46px;color:var(--green);line-height:1;
  }
  .product-word{position:absolute;left:0;top:0;width:702px;height:700px;pointer-events:none}
  .product-word text{font-family:"Fredoka",sans-serif;font-weight:600;font-size:98px;fill:var(--purple)}
  .audience{
    position:absolute;left:0;right:0;top:556px;text-align:center;line-height:1;
    font-weight:600;font-size:28px;color:var(--green);
  }
  .pets-art{
    position:absolute;left:151px;top:615px;width:385px;height:338px;
    background:linear-gradient(180deg,rgba(77,182,148,.6),var(--green));
    border-radius:150px 150px 0 0;
  }
  .info-band{
    position:absolute;left:0;right:0;bottom:0;height:167px;
    background:linear-gradient(180deg,var(--green),var(--green-deep));
  }
  .benefits{
    position:absolute;left:0;right:0;top:14px;text-align:center;line-height:1;
    font-weight:600;font-size:20px;color:var(--white);
  }
  .steps{position:absolute;left:0;right:0;top:46px;display:flex;justify-content:center;align-items:flex-start;gap:10px}
  .step{display:flex;flex-direction:column;align-items:center;width:96px}
  .step-icon{width:66px;height:66px;border-radius:50%;background:var(--white);display:flex;align-items:center;justify-content:center}
  .step-label{margin-top:6px;font-weight:600;font-size:15px;line-height:1;color:var(--white);white-space:nowrap}
  .step-link{display:flex;gap:6px;margin-top:30px}
  .step-link span{width:7px;height:7px;border-radius:50%;background:var(--white)}
</style>
</head>
<body>
  <main class="pouch-front">
    <div class="seal-line"></div>
    <h1 class="brand">VELUTRA</h1>
    <p class="descriptor-kicker">MINERAL</p>
    <p class="descriptor-main">INSTANT</p>
    <svg class="product-word" viewBox="0 0 702 700" aria-label="ABSORBER">
      <defs><path id="arch" d="M95 607 Q351 475 607 607"/></defs>
      <text text-anchor="middle"><textPath href="#arch" startOffset="50%" textLength="500" lengthAdjust="spacing">ABSORBER</textPath></text>
    </svg>
    <p class="audience">for Dogs &amp; Cats</p>
    <div class="pets-art" role="img" aria-label="Green silhouettes of a seated dog and cat seen from behind"></div>

    <section class="info-band">
      <p class="benefits">Fragrance-Free • 100% Mineral • Odor-Binding • Low-Dust</p>
      <div class="steps">
        <div class="step">
          <div class="step-icon">
            <svg width="38" height="42" viewBox="0 0 44 48" fill="var(--green)" aria-hidden="true">
              <rect x="8" y="4" width="14" height="7" rx="1"/>
              <path d="M22 5h6v4h-6z"/>
              <rect x="12" y="11" width="6" height="5"/>
              <path d="M9 16h12l3 8v20a2 2 0 0 1-2 2H8a2 2 0 0 1-2-2V24z"/>
              <circle cx="33" cy="4" r="1.4"/><circle cx="37" cy="7" r="1.4"/><circle cx="33" cy="10" r="1.4"/><circle cx="40" cy="3" r="1.2"/><circle cx="40" cy="11" r="1.2"/>
            </svg>
          </div>
          <span class="step-label">Sprinkle</span>
        </div>
        <div class="step-link"><span></span><span></span></div>
        <div class="step">
          <div class="step-icon">
            <svg width="44" height="44" viewBox="0 0 50 50" aria-hidden="true">
              <circle cx="25" cy="27" r="19" fill="none" stroke="var(--green)" stroke-width="2.5"/>
              <rect x="21" y="2" width="8" height="4" fill="var(--green)"/>
              <rect x="24" y="5" width="2" height="3" fill="var(--green)"/>
              <text x="25" y="29" text-anchor="middle" font-family="Barlow Semi Condensed, sans-serif" font-weight="700" font-size="13" fill="var(--green)">1–5</text>
              <text x="25" y="38" text-anchor="middle" font-family="Barlow Semi Condensed, sans-serif" font-weight="600" font-size="6" fill="var(--green)">min</text>
            </svg>
          </div>
          <span class="step-label">Wait 1–5 min</span>
        </div>
        <div class="step-link"><span></span><span></span></div>
        <div class="step">
          <div class="step-icon">
            <svg width="40" height="40" viewBox="0 0 46 46" fill="none" stroke="var(--green)" stroke-width="2.5" stroke-linejoin="round" aria-hidden="true">
              <path d="M6 10 L30 4 L40 30 L16 38 Z" fill="rgba(77,182,148,.15)"/>
              <path d="M14 42 V24 a3 3 0 0 1 6 0 V18 a3 3 0 0 1 6 0 v2 a3 3 0 0 1 6 0 v4 a3 3 0 0 1 6 0 v8 c0 6-4 10-10 10z"/>
            </svg>
          </div>
          <span class="step-label">Sweep</span>
        </div>
      </div>
    </section>
  </main>
</body>
</html>
```